2022 American Football Calendar Design

This project is for an American High School Football calendar for 2022.

The theme is US football and specifically high-school football for a streaming TV show about American high-school football.

The total number of pages will be 28 with the cover being 4 pages and the months being the other 24 pages.

Design Elements:

1. Each month will have 2 pages. 1 for the lead / hero image and one for the days of the month.

2. We will supply the images for each month of the calendar. There may be multiple potential image options for a given month. You can, as the designer, choose to use one or multiple images for the month if you feel the design would benefit.

3. Each month will have special days including US Holidays and special Football Days. We will supply a spreadsheet with all of these days and dates.

4. The boxes for the days should be square with enough space to allow for writing in the box when the calendar is printed.

5. Each month will also have a special quote text area that will contain special informational or an inspirational quote.

6. The calendar dimensions are 11" x 8 1/2" (US Letter - landscape orientation) - folded. So each page is US Letter size. A print guide template is attached from the printing company.

7. The title of the calendar is Pinebrook Rally 2022 Calendar.

For this contest please supply design concepts for the following:
1. Cover page;
2. Inside page;
3. Month Hero page;
4. Days of the month page;
5. Back cover page;

We will use these design concepts to choose the winner who will then need to finish the complete calendar design and preparation for printing.

Final Deliverables:

A. Complete 28 page calendar design - the winner will complete the design and layout of all pages.

B. Final print ready PDF at least 350 dpi with bleed for printing. Please see the attached size template from the printing company with guides.

C. Layered & Fully Editable Source File - InDesign, AI or PSD (NO COREL DRAW PLEASE - Adobe products only please). If vector files are supplied, we will also need a text editable version.

D. Any fonts used - we have licensing, if needed, available from Quillon Type and Marvesta Assets.

We are looking for a fast turnaround on this project so it can be sent to the printer next week.

Target Market(s)

High-school football players and their family & friends

Industry/Entity Type

American football

Font styles to use
Other font styles liked:
• Collegiate type sports fonts.

Colors

Designer to choose colors to be used in the design.

Requirements
Must have
• 350 DPI print-ready PDF, Fully editable source files including fonts & layers (NO Corel Draw) - see brief
Nice to have
• vector (AI) and PSD
Should not have
• Do not use Corel Draw

```html
<!DOCTYPE html>
<html lang="en">
<head>
<meta charset="utf-8">
<title>Pinebrook Rally 2022 Calendar</title>
<link href="https://fonts.googleapis.com/css2?family=Anton&family=Oswald:wght@500;700&family=Roboto+Condensed:wght@400;700&display=swap" rel="stylesheet">
<style>
  :root{
    --bg:#ececec;
    --paper:#ffffff;
    --red:#d7262e;
    --navy:#1f3a7a;
    --ink:#2b2b33;
    --line:#c9ccd6;
    --muted:#8a8f9c;
    --night-a:#0f1020;
    --night-b:#3a1e2e;
    --field-a:#56603a;
    --field-b:#6f7a48;
  }
  *{box-sizing:border-box;margin:0;padding:0}
  html,body{width:1200px;height:2180px;overflow:hidden}
  body{background:var(--bg);position:relative;font-family:"Roboto Condensed",Arial,sans-serif;color:var(--ink)}
  .page{position:absolute;left:80px;width:1040px;overflow:hidden;box-shadow:0 6px 18px rgba(0,0,0,.12)}

  /* Cover */
  .cover{top:40px;height:600px;background:var(--paper)}
  .cover-photo{position:absolute;inset:0;background:linear-gradient(180deg,#cfd8de 0%,#9fb39a 38%,#6f7f64 55%,#6d6d70 70%,#4a4a4e 100%)}
  .cover-brand{position:absolute;top:34px;left:0;right:0;display:flex;justify-content:center;align-items:center;gap:12px}
  .brand-dot{width:22px;height:22px;border-radius:50%;background:var(--navy)}
  .brand-name{font-family:"Oswald",Arial,sans-serif;font-weight:700;font-size:28px;letter-spacing:2px;color:var(--navy)}
  .cover-title{position:absolute;top:150px;left:0;right:0;text-align:center;font-family:"Anton",Impact,sans-serif;font-weight:400;color:var(--red);line-height:.95}
  .cover-title .name{display:block;font-size:96px;letter-spacing:3px}
  .cover-title .year{display:block;font-size:190px;letter-spacing:14px}

  /* Month hero */
  .hero{top:680px;height:300px;background:radial-gradient(ellipse at 45% 60%,#4b2a3c 0%,var(--night-b) 35%,var(--night-a) 80%)}

  /* Days sheet */
  .sheet{background:var(--paper);padding:24px 36px}
  .sheet-jan{top:980px;height:440px}
  .sheet-feb{top:1460px;height:360px}
  .sheet-head{display:flex;align-items:center;justify-content:space-between;height:50px;border-bottom:3px solid var(--navy);margin-bottom:6px}
  .month{font-family:"Oswald",Arial,sans-serif;font-weight:700;font-size:30px;letter-spacing:3px;color:var(--navy)}
  .month .yr{color:var(--red);margin-left:10px}
  .sheet-brand{display:flex;align-items:center;gap:8px}
  .sheet-brand .brand-dot{width:14px;height:14px}
  .sheet-brand .brand-name{font-size:16px;letter-spacing:1.5px}
  .weekdays,.days{display:grid;grid-template-columns:repeat(7,1fr)}
  .weekdays span{height:26px;font-family:"Oswald",Arial,sans-serif;font-weight:500;font-size:13px;letter-spacing:2px;color:var(--navy);text-align:center;line-height:26px}
  .days{border-top:1px solid var(--line);border-left:1px solid var(--line)}
  .days span{border-right:1px solid var(--line);border-bottom:1px solid var(--line);font-size:13px;font-weight:700;color:var(--muted);padding:4px 6px}
  .sheet-jan .days span{height:50px}
  .sheet-feb .days span{height:46px}

  /* Quote page */
  .quote-page{top:1820px;height:320px}
  .quote-backdrop{position:absolute;inset:0;background:linear-gradient(135deg,var(--field-b),var(--field-a))}
  .quote-photo{position:absolute;left:40px;top:40px;width:220px;height:240px;background:linear-gradient(160deg,#7b8699,#3d4658)}
  .quote{position:absolute;left:300px;right:50px;top:60px;font-family:"Anton",Impact,sans-serif;font-weight:400;font-size:46px;line-height:1.12;letter-spacing:1px;color:#ffffff;text-transform:uppercase}
</style>
</head>
<body>

<section class="page cover">
  <div class="cover-photo" role="img" aria-label="Photo of a young football player walking down a tree-lined road toward the field"></div>
  <div class="cover-brand"><span class="brand-dot"></span><span class="brand-name">HOLLOWFIELD ATHLETICS</span></div>
  <h1 class="cover-title"><span class="name">PINEBROOK RALLY</span><span class="year">2022</span></h1>
</section>

<section class="page hero" role="img" aria-label="Night photo of a football player in helmet under stadium lights"></section>

<section class="page sheet sheet-jan">
  <header class="sheet-head">
    <h2 class="month">JANUARY<span class="yr">2022</span></h2>
    <div class="sheet-brand"><span class="brand-dot"></span><span class="brand-name">HOLLOWFIELD ATHLETICS</span></div>
  </header>
  <div class="weekdays"><span>SUN</span><span>MON</span><span>TUE</span><span>WED</span><span>THU</span><span>FRI</span><span>SAT</span></div>
  <div class="days">
    <span></span><span></span><span></span><span></span><span></span><span></span><span>1</span>
    <span>2</span><span>3</span><span>4</span><span>5</span><span>6</span><span>7</span><span>8</span>
    <span>9</span><span>10</span><span>11</span><span>12</span><span>13</span><span>14</span><span>15</span>
    <span>16</span><span>17</span><span>18</span><span>19</span><span>20</span><span>21</span><span>22</span>
    <span>23</span><span>24</span><span>25</span><span>26</span><span>27</span><span>28</span><span>29</span>
    <span>30</span><span>31</span><span></span><span></span><span></span><span></span><span></span>
  </div>
</section>

<section class="page sheet sheet-feb">
  <header class="sheet-head">
    <h2 class="month">FEBRUARY<span class="yr">2022</span></h2>
    <div class="sheet-brand"><span class="brand-dot"></span><span class="brand-name">HOLLOWFIELD ATHLETICS</span></div>
  </header>
  <div class="weekdays"><span>SUN</span><span>MON</span><span>TUE</span><span>WED</span><span>THU</span><span>FRI</span><span>SAT</span></div>
  <div class="days">
    <span></span><span></span><span>1</span><span>2</span><span>3</span><span>4</span><span>5</span>
    <span>6</span><span>7</span><span>8</span><span>9</span><span>10</span><span>11</span><span>12</span>
    <span>13</span><span>14</span><span>15</span><span>16</span><span>17</span><span>18</span><span>19</span>
    <span>20</span><span>21</span><span>22</span><span>23</span><span>24</span><span>25</span><span>26</span>
    <span>27</span><span>28</span><span></span><span></span><span></span><span></span><span></span>
  </div>
</section>

<section class="page quote-page">
  <div class="quote-backdrop" role="img" aria-label="Photo of a football field turf with yard lines"></div>
  <div class="quote-photo" role="img" aria-label="Photo of a player on the sideline"></div>
  <p class="quote">Keep your face always toward the sunshine and shadows will fall behind you</p>
</section>

</body>
</html>
```